40k Ultra High Pressure Waterblasing Ad

We need 1 page flyer ad for our industry's brochure/membership directory.
We're a manufacturer & supplier for the Ultra High Pressure Waterblasting industry.
We'd like the ad to be simple and clean, highlighting some of our parts. Our dedication to our customers and affordable prices.
Some of the parts are Dorvel Mastrick Hoses, Sapphire Nozzles, Rotating Jetlance.

Our website is torvaflux.com

Requirements
Must have
• Dorvel Mastrick 40k Hose
• Sapphire Nozzles
• Rotating Jetlance
• **Update - Would like to incorporate the "iron skein logo w/ bulldog" from uploaded dorvel iron skein hose attachment. Highlighting the hose's features.
Nice to have
• Brief Bullet points or something else highlighting what we sell.
• - Pump replacement parts
• - Sapphire Nozzles
• - Rotating Jetlance
• - Fittings and adapters
• - Safety Gear
• I've uploaded past ads we've used.
Should not have
• Lots of text area

```html
<!DOCTYPE html>
<html lang="en">
<head>
<meta charset="utf-8">
<title>Torvaflux Technologies – Ultra High Pressure Flyer</title>
<link rel="stylesheet" href="https://fonts.googleapis.com/css2?family=Bebas+Neue&family=Montserrat:wght@500;600;700&family=Roboto+Condensed:wght@400&family=Arimo:wght@400;700&display=swap">
<style>
  :root{
    --navy:#0f2a44;
    --navy-deep:#0b2138;
    --blue:#1d6fe0;
    --blue-bright:#2a86f5;
    --paper:#f4f5f7;
    --paper-shade:#dfe2e6;
    --ink:#13304f;
    --white:#ffffff;
  }
  *{margin:0;padding:0;box-sizing:border-box}
  html,body{width:946px;height:1200px;overflow:hidden;background:#cfcfcf}
  .flyer{position:relative;width:946px;height:1200px;overflow:hidden;background:var(--paper);font-family:"Montserrat",sans-serif}
  .backdrop{position:absolute;inset:0}
  .brand{position:absolute;left:40px;top:40px;width:360px;text-align:center}
  .brand-name{font-family:"Montserrat",sans-serif;font-weight:700;font-size:118px;line-height:1;color:var(--white);letter-spacing:2px}
  .brand-company{position:absolute;left:36px;top:210px;font-family:"Arimo",sans-serif;font-size:22px;color:var(--white)}
  .brand-phone{position:absolute;left:72px;top:236px;font-family:"Arimo",sans-serif;font-size:31px;color:var(--blue-bright)}
  .headline{position:absolute;left:52px;top:574px;font-family:"Bebas Neue",sans-serif;font-size:80px;line-height:68px;color:var(--navy)}
  .headline .accent{color:var(--blue)}
  .products-title{position:absolute;left:530px;top:489px;width:370px;height:52px;border:1.5px dashed #8fb2e4;border-radius:3px;text-align:center;font-weight:700;font-size:31px;line-height:48px;color:var(--blue)}
  .checklist{position:absolute;left:530px;list-style:none}
  .checklist li{display:flex;align-items:center;gap:20px;height:31px;font-weight:700;font-size:20.5px;color:var(--ink)}
  .checklist svg{width:22px;height:22px;flex:none}
  .products-list{top:557px}
  .features-list{top:817px;}
  .features-list li{height:32px}
  .supplier-note{position:absolute;left:530px;top:724px;width:390px;font-weight:600;font-size:15.5px;line-height:23px;color:var(--ink)}
  .contact-title{position:absolute;left:467px;top:1102px;width:450px;font-weight:600;font-size:40px;letter-spacing:1px;color:var(--white);text-align:center}
  .contact-rule{position:absolute;left:467px;top:1156px;width:448px;height:1px;background:#9fb0c4}
  .contact-row{position:absolute;left:467px;top:1160px;width:450px;display:flex;justify-content:space-between;align-items:center;font-family:"Roboto Condensed",sans-serif;font-size:15px;color:var(--white)}
  .contact-row span{display:flex;align-items:center;gap:6px}
  .contact-row svg{width:12px;height:12px}
</style>
</head>
<body>
<main class="flyer">
  <svg class="backdrop" viewBox="0 0 946 1200" width="946" height="1200">
    <defs>
      <linearGradient id="paperGrad" x1="0" y1="0" x2="1" y2="0">
        <stop offset="0" stop-color="#fafafa"/><stop offset="0.55" stop-color="#eceef1"/><stop offset="1" stop-color="#dfe2e6"/>
      </linearGradient>
      <linearGradient id="rigGrad" x1="0" y1="0" x2="0" y2="1">
        <stop offset="0" stop-color="#3a2a22"/><stop offset="0.55" stop-color="#7a4a2a"/><stop offset="0.8" stop-color="#e08a2e"/><stop offset="1" stop-color="#4a2a18"/>
      </linearGradient>
      <linearGradient id="hoseGrad" x1="0" y1="0" x2="0" y2="1">
        <stop offset="0" stop-color="#c9cdd2"/><stop offset="1" stop-color="#7d848c"/>
      </linearGradient>
      <linearGradient id="metalGrad" x1="0" y1="0" x2="1" y2="0">
        <stop offset="0" stop-color="#8a7c6c"/><stop offset="0.5" stop-color="#d6d2cc"/><stop offset="1" stop-color="#7d7163"/>
      </linearGradient>
      <linearGradient id="planeGrad" x1="0" y1="0" x2="0" y2="1">
        <stop offset="0" stop-color="#f2f2f2"/><stop offset="0.5" stop-color="#b9bcc0"/><stop offset="1" stop-color="#6f7276"/>
      </linearGradient>
      <clipPath id="rigClip"><circle cx="805" cy="140" r="312"/></clipPath>
    </defs>

    <rect class="paper" width="946" height="1200" fill="url(#paperGrad)"/>

    <!-- top navy field with wave -->
    <path class="blue-wave" d="M0 378 Q260 330 500 420 Q640 470 946 455 V480 Q640 500 500 445 Q260 360 0 410 Z" fill="var(--blue)"/>
    <path class="navy-field" d="M0 0 H946 V450 Q640 465 500 410 Q260 320 0 372 Z" fill="var(--navy)"/>

    <!-- rig photo circle -->
    <circle cx="805" cy="140" r="332" fill="var(--blue)"/>
    <circle cx="805" cy="140" r="320" fill="#d9dde2"/>
    <g role="img" aria-label="Photo of an offshore oil platform at sunset">
      <rect x="480" y="0" width="466" height="460" fill="url(#rigGrad)" clip-path="url(#rigClip)"/>
    </g>

    <!-- hose photo -->
    <g role="img" aria-label="Photo of a coiled grey ultra high pressure hose">
      <ellipse cx="228" cy="410" rx="190" ry="118" fill="url(#hoseGrad)"/>
    </g>

    <!-- nozzles photo -->
    <g role="img" aria-label="Photo of stainless steel sapphire nozzles and fittings">
      <rect x="52" y="802" width="366" height="112" rx="30" fill="url(#metalGrad)"/>
    </g>

    <!-- airplane photo -->
    <path d="M0 958 Q300 880 470 1200 H0 Z" fill="var(--blue)"/>
    <path d="M0 968 Q285 900 452 1200 H0 Z" fill="#e3e6ea"/>
    <g role="img" aria-label="Photo of a jet airliner on a runway">
      <path d="M0 978 Q270 918 434 1200 H0 Z" fill="url(#planeGrad)"/>
    </g>

    <!-- jetlance photo -->
    <g role="img" aria-label="Photo of a rotating jetlance tool">
      <rect x="500" y="916" width="272" height="150" rx="12" fill="url(#metalGrad)" opacity="0.85"/>
    </g>

    <!-- bottom navy band -->
    <path class="navy-band" d="M417 1200 V1078 H830 Q920 1068 946 990 V1200 Z" fill="var(--navy)"/>

    <!-- partner and origin badges -->
    <g class="partner-badge">
      <rect x="798" y="925" width="98" height="34" fill="#111"/>
      <rect x="798" y="959" width="98" height="15" fill="#b9bcc0"/>
    </g>
    <circle class="origin-badge" cx="850" cy="1044" r="44" fill="#d7dbe0" stroke="var(--blue)" stroke-width="4"/>
  </svg>

  <div class="brand"><div class="brand-name">TFX</div></div>
  <div class="brand-company">Torvaflux Technologies, Inc.</div>
  <div class="brand-phone">555-014-2290</div>

  <h1 class="headline">WHEN THE<br>PRESSURES ON<br><span class="accent">CHOOSE TFX</span></h1>

  <div class="products-title">OUR PRODUCTS</div>
  <ul class="checklist products-list">
    <li><svg viewBox="0 0 22 22"><circle cx="11" cy="11" r="9" fill="none" stroke="var(--blue)" stroke-width="2.4"/><path d="M6 11 l4 4 l9-10" fill="none" stroke="var(--blue)" stroke-width="2.6"/></svg>PUMP REPLACEMENT PARTS</li>
    <li><svg viewBox="0 0 22 22"><circle cx="11" cy="11" r="9" fill="none" stroke="var(--blue)" stroke-width="2.4"/><path d="M6 11 l4 4 l9-10" fill="none" stroke="var(--blue)" stroke-width="2.6"/></svg>SAPPHIRE NOZZLES</li>
    <li><svg viewBox="0 0 22 22"><circle cx="11" cy="11" r="9" fill="none" stroke="var(--blue)" stroke-width="2.4"/><path d="M6 11 l4 4 l9-10" fill="none" stroke="var(--blue)" stroke-width="2.6"/></svg>ROTATING JETLANCE</li>
    <li><svg viewBox="0 0 22 22"><circle cx="11" cy="11" r="9" fill="none" stroke="var(--blue)" stroke-width="2.4"/><path d="M6 11 l4 4 l9-10" fill="none" stroke="var(--blue)" stroke-width="2.6"/></svg>FITTINGS AND ADAPTERS</li>
    <li><svg viewBox="0 0 22 22"><circle cx="11" cy="11" r="9" fill="none" stroke="var(--blue)" stroke-width="2.4"/><path d="M6 11 l4 4 l9-10" fill="none" stroke="var(--blue)" stroke-width="2.6"/></svg>SAFETY GEAR</li>
  </ul>

  <p class="supplier-note">Leading Supplier of Dorvel Mastrick Ultra High Pressure Hoses" Stocking All your 40k and 55k Ultra High Pressures Hoses</p>

  <ul class="checklist features-list">
    <li><svg viewBox="0 0 22 22"><circle cx="11" cy="11" r="9" fill="none" stroke="var(--blue)" stroke-width="2.4"/><path d="M6 11 l4 4 l9-10" fill="none" stroke="var(--blue)" stroke-width="2.6"/></svg>IRON SKEIN</li>
    <li><svg viewBox="0 0 22 22"><circle cx="11" cy="11" r="9" fill="none" stroke="var(--blue)" stroke-width="2.4"/><path d="M6 11 l4 4 l9-10" fill="none" stroke="var(--blue)" stroke-width="2.6"/></svg>ABRASION COVER</li>
    <li><svg viewBox="0 0 22 22"><circle cx="11" cy="11" r="9" fill="none" stroke="var(--blue)" stroke-width="2.4"/><path d="M6 11 l4 4 l9-10" fill="none" stroke="var(--blue)" stroke-width="2.6"/></svg>BURST SHIELD</li>
  </ul>

  <div class="contact-title">CONTACT US TODAY</div>
  <div class="contact-rule"></div>
  <div class="contact-row">
    <span><svg viewBox="0 0 12 12"><rect x="1" y="2.5" width="10" height="7" fill="none" stroke="#fff"/><path d="M1 3 l5 4 l5-4" fill="none" stroke="#fff"/></svg>info@torvaflux.com</span>
    <span><svg viewBox="0 0 12 12"><path d="M3 1 l2 2.5 l-1.2 1.5 q1 2 3 3 l1.5-1.2 l2.5 2 l-1.5 2 q-5 0-8.5-8.5 z" fill="none" stroke="#fff"/></svg>555-014-2290</span>
    <span><svg viewBox="0 0 12 12"><circle cx="6" cy="6" r="5" fill="none" stroke="#fff"/><path d="M1 6 h10 M6 1 q-3 5 0 10 q3-5 0-10" fill="none" stroke="#fff"/></svg>www.torvaflux.com</span>
  </div>
</main>
</body>
</html>
```